Webdesign für psychotherapeutische Praxis
Zielgruppe
Psychotherapeutische Praxis für erwachsene Patienten mit psychischen Erkrankungen.
Die Website soll eine solide, vertrauensvolle Information über das therapeutische Angebot bieten sowie alle Informationen zur Erstkontaktaufnahme erhalten.
Aufgabenstellung
Logo füge ich bei. Die Farben, das Design, die Schrift sollen dem Logo entsprechen (Grau, Violett-Pink Töne, moderne Schrift).

```html
<!DOCTYPE html>
<html lang="de">
<head>
<meta charset="utf-8">
<title>Psychotherapeutische Praxis Hollmann – Kontakt</title>
<link href="https://fonts.googleapis.com/css2?family=Ubuntu:wght@300;400;500&display=swap" rel="stylesheet">
<style>
  :root {
    --text: #3f3f42;
    --footer-bg: #4a4849;
    --footer-text: #f2f2f2;
    --accent: #a45bbf;
    --map-base: #ececec;
    --photo-top: #d88a68;
    --photo-mid: #e7c6bb;
    --photo-low: #5f7d45;
  }
  * { box-sizing: border-box; margin: 0; padding: 0; }
  html, body { width: 1067px; height: 1200px; overflow: hidden; background: #fff; }
  body { position: relative; font-family: "Ubuntu", sans-serif; font-weight: 300; color: var(--text); }

  .site-header { position: absolute; top: 0; left: 0; width: 1067px; height: 56px; background: #fff; }
  .brand { position: absolute; left: 118px; top: 10px; display: flex; align-items: center; gap: 10px; }
  .brand-mark { width: 34px; height: 34px; border-radius: 50%; background: var(--accent); }
  .brand-text { font-size: 7.5px; line-height: 10px; color: var(--text); font-weight: 400; }
  .brand-text small { display: block; font-size: 4px; line-height: 6px; }
  .main-nav a { position: absolute; top: 21px; font-size: 13px; font-weight: 400; color: var(--text); text-decoration: none; }

  .map { position: absolute; top: 56px; left: 0; width: 1067px; height: 277px; background: var(--map-base); }

  .contact-list { position: absolute; left: 130px; top: 395px; }
  .contact-item { position: absolute; left: 0; font-size: 19.5px; line-height: 22px; font-weight: 400; white-space: nowrap; }
  .contact-item svg { position: absolute; left: 0; }
  .contact-item span { position: absolute; left: 44px; }

  .office-photo { position: absolute; left: 632px; top: 379px; width: 323px; height: 431px;
    background: linear-gradient(180deg, var(--photo-top) 0%, var(--photo-mid) 35%, #b8b2ad 60%, var(--photo-low) 85%); }

  .availability { position: absolute; left: 118px; top: 636px; width: 475px; height: 321px; overflow: hidden; }
  .availability h2 { font-size: 18.5px; font-weight: 400; line-height: 24px; margin-bottom: 8px; }
  .availability p { font-size: 15.4px; line-height: 19.5px; margin-bottom: 19px; }

  .site-footer { position: absolute; left: 0; top: 957px; width: 1067px; height: 243px; background: var(--footer-bg); color: var(--footer-text); }
  .footer-col { position: absolute; top: 50px; }
  .footer-col h3 { display: inline-block; font-size: 16px; font-weight: 400; padding-bottom: 5px; border-bottom: 1px solid var(--footer-text); margin-bottom: 8px; }
  .footer-col p { font-size: 13.5px; line-height: 17px; }
  .footer-item { position: relative; padding-left: 26px; font-size: 13.5px; line-height: 17px; margin-top: 10px; }
  .footer-item svg { position: absolute; left: 0; top: 0; }
</style>
</head>
<body>
  <header class="site-header">
    <div class="brand">
      <div class="brand-mark"></div>
      <div class="brand-text">Psychotherapeutische Praxis<br>DIPL.-PSYCH. KARIN HOLLMANN<small>Psychologische Psychotherapeutin (VT)</small></div>
    </div>
    <nav class="main-nav">
      <a href="#" style="left:354px">Startseite</a>
      <a href="#" style="left:467px">Therapieangebot</a>
      <a href="#" style="left:633px">Therapieablauf</a>
      <a href="#" style="left:781px">Über mich</a>
      <a href="#" style="left:885px">Kontakt</a>
    </nav>
  </header>

  <div class="map" role="img" aria-label="Stadtplan mit markiertem Praxisstandort"></div>

  <section class="contact-list">
    <div class="contact-item" style="top:0">
      <svg width="22" height="30" viewBox="0 0 22 30"><path d="M11 2a8.5 8.5 0 0 0-8.5 8.5C2.5 17 11 28 11 28s8.5-11 8.5-17.5A8.5 8.5 0 0 0 11 2z" fill="none" stroke="var(--text)" stroke-width="2.4"/><circle cx="11" cy="10.5" r="2.5" fill="var(--text)"/></svg>
      <span>Lindenhofgasse 17<br>60488 Frankfurt/Main</span>
    </div>
    <div class="contact-item" style="top:62px">
      <svg width="28" height="28" viewBox="0 0 28 28"><path d="M2 8c4-5 20-5 24 0l-3 3-4-2V6H9v3l-4 2z" fill="var(--text)"/><g fill="var(--text)"><circle cx="9" cy="14" r="1.6"/><circle cx="14" cy="14" r="1.6"/><circle cx="19" cy="14" r="1.6"/><circle cx="9" cy="19" r="1.6"/><circle cx="14" cy="19" r="1.6"/><circle cx="19" cy="19" r="1.6"/><circle cx="14" cy="24" r="1.6"/></g></svg>
      <span>0170/204 57 31</span>
    </div>
    <div class="contact-item" style="top:108px">
      <svg width="28" height="28" viewBox="0 0 28 28"><path d="M26 2 2 12l9 4 4 10z M26 2 11 16" fill="none" stroke="var(--text)" stroke-width="2" stroke-linejoin="round"/></svg>
      <span>hollmanntherap@postfach.de</span>
    </div>
  </section>

  <div class="office-photo" role="img" aria-label="Foto des Fachwerkhauses mit Praxiseingang und Garten"></div>

  <section class="availability">
    <h2>Telefonische Erreichbarkeit:</h2>
    <p>Meine telefonischen Sprechzeiten sind montags,<br>dienstags, mittwochs und donnerstags von 13:00 bis<br>13:30 Uhr.</p>
    <p style="margin-top:32px">Sollten Sie mich nicht persönlich erreichen, hinterlassen Sie bitte eine Nachricht auf dem Anrufbeantworter oder senden Sie mir eine E-mail. Beachten Sie hierzu folgendes Hinweis zum Datenschutz:</p>
    <p style="margin-top:12px">Durch das Versenden einer E-Mail erklären Sie sich mit der Korrespondenz bzw. der Zusendung von personenbezogenen- und Gesundheitsdaten per E-Mail auf die von Ihnen verwendete E-</p>
  </section>

  <footer class="site-footer">
    <div class="footer-col" style="left:221px">
      <h3>Psychotherapeutische Praxis Hollmann</h3>
      <div class="footer-item">
        <svg width="16" height="24" viewBox="0 0 22 30"><path d="M11 2a8.5 8.5 0 0 0-8.5 8.5C2.5 17 11 28 11 28s8.5-11 8.5-17.5A8.5 8.5 0 0 0 11 2z" fill="none" stroke="var(--footer-text)" stroke-width="2.6"/></svg>
        Lindenhofgasse 17<br>60488 Frankfurt/Main
      </div>
      <div class="footer-item">
        <svg width="19" height="19" viewBox="0 0 28 28"><path d="M2 8c4-5 20-5 24 0l-3 3-4-2V6H9v3l-4 2z" fill="var(--footer-text)"/><g fill="var(--footer-text)"><circle cx="9" cy="14" r="1.6"/><circle cx="14" cy="14" r="1.6"/><circle cx="19" cy="14" r="1.6"/><circle cx="9" cy="19" r="1.6"/><circle cx="14" cy="19" r="1.6"/><circle cx="19" cy="19" r="1.6"/><circle cx="14" cy="24" r="1.6"/></g></svg>
        0170 / 204 57 31
      </div>
      <div class="footer-item" style="margin-top:15px">
        <svg width="18" height="18" viewBox="0 0 28 28"><path d="M26 2 2 12l9 4 4 10z M26 2 11 16" fill="none" stroke="var(--footer-text)" stroke-width="2" stroke-linejoin="round"/></svg>
        hollmanntherap@postfach.de
      </div>
    </div>
    <div class="footer-col" style="left:566px">
      <h3 style="padding-right:46px">Hinweis</h3>
      <p>Aufgrund der&nbsp; Coronavirus /SARS-CoV-2- Krise<br>biete ich zertifizierte Videosprechstunden an!</p>
      <h3 style="margin-top:12px">Telefonische Erreichbarkeit</h3>
      <p>Montags, dienstags, Mittwochs &amp; Donnerstags<br>von 13:00 bis 13:30 Uhr</p>
    </div>
  </footer>
</body>
</html>
```